Nice, modern, and professional credit repair website

We're a new credit repair company and we need a website to inform our prospective clients about the service we provide. We wan't it to catch the attention of the people as well as it be informative of the different types of derogatory items that can be listed on a report. Please refer to ( www.pathtoprime.example ) for an idea of what I'm looking for.

Colors
0455a3
0293ce
33a6d7
ffffff

Requirements
Must have
• The website must include information regarding credit repair. We'd like the website to include modern colors similar to that of our logo.
A link to our Facebook page. Www.facebook.com/brevantaledgerpartners
A link to our Instagram page: @BrevantaLedgerPartners
A link to our Snapchat page: Brevanta-Ledger
Also, we'd like to have an area where clients would fill out basic information where we could reach out to them.
Nice to have
• Images of new homes, cars, credit cards (Should NOT endorse Quilo, TF, BRONT, or Palvenry.)

```html
<!DOCTYPE html>
<html lang="en">
<head>
<meta charset="utf-8">
<title>Brevanta Ledger – Credit Repair</title>
<link href="https://fonts.googleapis.com/css2?family=Montserrat:wght@400;500;600;700;800&family=Open+Sans:wght@400;600&display=swap" rel="stylesheet">
<style>
:root{
  --navy:#0a2a5c;
  --deep:#0455a3;
  --sky:#0293ce;
  --light:#33a6d7;
  --white:#ffffff;
  --ink:#1d2433;
  --muted:#6b7383;
  --paper:#f3f5f8;
  --line:#dfe4ea;
  --footer:#0b1d45;
}
*{box-sizing:border-box;margin:0;padding:0}
html,body{width:1200px;height:4736px;overflow:hidden}
body{font-family:"Open Sans",Arial,sans-serif;color:var(--ink);background:var(--white);font-size:14px}
h1,h2,h3,h4,.btn,.nav,.brand{font-family:"Montserrat",Arial,sans-serif}
.btn{display:inline-block;background:var(--deep);color:var(--white);font-size:14px;font-weight:600;padding:14px 30px;border-radius:3px;text-decoration:none}
.accent{color:var(--deep)}
.center{text-align:center}

/* top bar */
.topbar{height:24px;background:var(--deep);color:var(--white);font-size:11px;display:flex;align-items:center;padding:0 60px;gap:40px}
.topbar .social{margin-left:auto;display:flex;gap:8px;align-items:center}
.topbar .dot{width:10px;height:10px;border-radius:50%;background:var(--white)}

/* header */
.header{height:72px;display:flex;align-items:center;padding:0 60px;background:var(--white)}
.brand{display:flex;align-items:center;gap:12px;font-weight:700;font-size:22px;color:var(--deep)}
.brand .mark{width:36px;height:36px;border-radius:50%;background:var(--deep)}
.nav{margin-left:auto;display:flex;align-items:center;gap:26px;font-size:14px;font-weight:500;color:var(--ink)}
.nav .btn{padding:10px 20px;font-size:13px}
.nav .btn.dark{background:var(--navy)}

/* hero */
.hero{position:relative;height:544px}
.hero-photo{position:absolute;inset:0;background:linear-gradient(90deg,#f4f3f1 0%,#ecebe8 38%,#c9b7a6 62%,#8d6f58 82%,#5b4638 100%)}
.hero-copy{position:absolute;left:130px;top:130px;width:420px}
.hero h1{font-size:44px;line-height:1.2;font-weight:800;color:var(--navy)}
.hero h1 span{color:var(--deep)}
.hero p{margin:22px 0 30px;font-size:16px;line-height:1.5;color:var(--ink)}

/* how it works */
.how{height:480px;padding-top:80px}
.how h2,.improve h2,.pricing h2,.faq h2,.inquiry h2{font-size:36px;font-weight:700;color:var(--navy)}
.steps{display:flex;justify-content:center;align-items:flex-start;gap:20px;margin-top:70px}
.step{width:200px;text-align:center;font-family:"Montserrat",sans-serif;font-size:16px;font-weight:500}
.ring{width:112px;height:112px;margin:0 auto 18px;border-radius:50%;border:3px solid #d6dce4;border-left-color:var(--navy);display:flex;align-items:center;justify-content:center}
.arrow{margin-top:30px}
.how .btn{margin-top:42px}

/* improve */
.improve{height:870px;background:var(--paper);padding-top:90px}
.improve h2{line-height:1.35}
.cards{display:grid;grid-template-columns:repeat(3,280px);gap:30px 40px;justify-content:center;margin-top:50px}
.card{background:var(--white);border-radius:4px;height:250px;padding:40px 26px;text-align:center;box-shadow:0 2px 10px rgba(10,42,92,.08)}
.card h3{font-size:16px;font-weight:600;margin:14px 0 10px;color:var(--ink)}
.card p{font-size:13px;line-height:1.5;color:var(--muted)}
.card.active{background:var(--light)}
.card.active h3,.card.active p{color:var(--white)}
.improve .btn{margin-top:48px}

/* guarantee */
.guarantee{height:440px;background:linear-gradient(120deg,var(--deep) 0%,#1f6fbd 45%,var(--light) 100%);color:var(--white);text-align:center;padding-top:150px}
.guarantee h2{font-size:40px;font-weight:700;line-height:1.2}
.guarantee p{width:640px;margin:26px auto 30px;font-size:15px;line-height:1.6}
.guarantee .btn{background:var(--sky)}

/* pricing */
.pricing{height:900px;padding-top:80px}
.pricing .eyebrow{font-family:"Montserrat",sans-serif;font-size:13px;font-weight:600;color:var(--ink);letter-spacing:.5px}
.pricing h2{margin-top:6px}
.plans{display:flex;justify-content:center;gap:60px;margin-top:50px}
.plan{width:330px;height:702px;background:var(--white);box-shadow:0 4px 18px rgba(10,42,92,.12);border-bottom:6px solid var(--sky);padding:40px 34px;text-align:center}
.plan .price{font-family:"Montserrat",sans-serif;font-size:42px;font-weight:700;color:var(--navy);margin-top:16px}
.plan .price small{font-size:20px}
.plan .sub{font-size:13px;color:var(--muted);margin-top:4px}
.plan .term{font-family:"Montserrat",sans-serif;font-weight:600;font-size:15px;margin-top:6px}
.includes{background:#e3ecf6;color:var(--deep);font-family:"Montserrat",sans-serif;font-weight:600;font-size:14px;padding:10px;margin:26px 0 26px;border-radius:3px}
.features{list-style:none;text-align:left}
.features li{font-size:14px;padding:9px 0 9px 24px;position:relative;color:var(--ink)}
.features li::before{content:"";position:absolute;left:4px;top:16px;width:8px;height:8px;border-radius:50%;background:var(--sky)}
.plan .btn{margin-top:40px}

/* faq */
.faq{height:570px;padding-top:50px;background:var(--paper)}
.faq-list{width:780px;margin:50px auto 0}
.faq-item{background:var(--white);border:1px solid var(--line);padding:14px 20px;margin-bottom:8px;display:flex;justify-content:space-between;align-items:center;font-size:15px;font-family:"Montserrat",sans-serif;font-weight:500}
.faq-item .toggle{width:20px;height:20px;border-radius:50%;border:1px solid #9aa5b4;flex-shrink:0}
.faq-item.open{display:block;background:#e6edf5}
.faq-item.open .q{display:flex;justify-content:space-between}
.faq-item.open .toggle{background:var(--deep);border-color:var(--deep)}
.faq-item.open p{font-family:"Open Sans",sans-serif;font-weight:400;font-size:13px;color:var(--muted);margin-top:8px;line-height:1.5}

/* inquiry */
.inquiry{height:530px;padding-top:80px}
.form{width:760px;margin:50px auto 0;display:grid;grid-template-columns:1fr 1fr;gap:16px 24px}
.fields{display:flex;flex-direction:column;gap:16px}
.field{border:1px solid var(--line);height:50px;padding:14px;font-size:13px;color:var(--muted)}
.field.message{height:182px}
.inquiry .btn{margin-top:34px;padding:12px 28px}

/* footer */
.footer{height:270px;background:var(--footer);color:var(--white);display:flex;padding:60px 130px 0;gap:70px}
.footer h4{font-size:16px;font-weight:600;margin-bottom:20px}
.footer p,.footer li{font-size:12px;line-height:1.7;color:#c6cfe0}
.footer ul{list-style:none}
.footer .mission{width:220px}
.contact li{display:flex;align-items:center;gap:10px;margin-bottom:10px}
.contact .ic{width:22px;height:22px;border-radius:50%;border:1px solid #c6cfe0;display:flex;align-items:center;justify-content:center}
.footer-brand{margin-left:auto;text-align:center}
.footer-brand .name{font-family:"Montserrat",sans-serif;font-weight:700;font-size:18px}
.footer-brand .mark{width:90px;height:90px;border-radius:50%;border:3px solid var(--white);margin:0 auto 14px}
.socials{display:flex;gap:10px;justify-content:center;margin-top:14px}
.socials span{width:28px;height:28px;border-radius:50%;border:1px solid var(--white)}
.copyright{height:46px;background:var(--deep);color:var(--white);font-size:12px;display:flex;align-items:center;justify-content:center}
</style>
</head>
<body>

<div class="topbar">
  <span>Monday – Friday: 9am – 6pm</span>
  <span>Location: Lorem Ipsum</span>
  <span>Call Us: 555-014-2290</span>
  <span class="social">Visit our social pages <i class="dot"></i><i class="dot"></i><i class="dot"></i></span>
</div>

<header class="header">
  <div class="brand"><span class="mark"></span>Brevanta Ledger</div>
  <nav class="nav">
    <span>Home</span><span>Pricing</span><span>Blog</span><span>About Us</span><span>Contact Us</span>
    <a class="btn" href="#">Get Started</a>
    <a class="btn dark" href="#">Login</a>
  </nav>
</header>

<section class="hero">
  <div class="hero-photo" role="img" aria-label="Couple smiling at a laptop while holding a credit card"></div>
  <div class="hero-copy">
    <h1>Repair Your Credit<br><span>With The Experts</span></h1>
    <p>We are a new credit repair company and want website to inform our prospective clients about the service we provide.</p>
    <a class="btn" href="#">Get Started</a>
  </div>
</section>

<section class="how center">
  <h2>How It <span class="accent">Works</span></h2>
  <div class="steps">
    <div class="step">
      <div class="ring"><svg width="44" height="44" viewBox="0 0 44 44" fill="none" stroke="#0455a3" stroke-width="2.5"><rect x="6" y="6" width="32" height="32" rx="3"/><line x1="12" y1="15" x2="32" y2="15"/><line x1="12" y1="22" x2="32" y2="22"/><line x1="12" y1="29" x2="24" y2="29"/></svg></div>
      Enroll
    </div>
    <svg class="arrow" width="90" height="40" viewBox="0 0 90 40" fill="none" stroke="#9aa5b4" stroke-width="1.5"><path d="M4 30 Q45 0 80 26"/><path d="M72 22 L80 26 L74 33"/></svg>
    <div class="step">
      <div class="ring"><svg width="44" height="44" viewBox="0 0 44 44" fill="none" stroke="#0455a3" stroke-width="2.5"><rect x="6" y="6" width="32" height="24" rx="2"/><line x1="22" y1="30" x2="14" y2="40"/><line x1="22" y1="30" x2="30" y2="40"/><polyline points="12,24 19,16 24,20 32,12"/></svg></div>
      Learn New Strategists
    </div>
    <svg class="arrow" width="90" height="40" viewBox="0 0 90 40" fill="none" stroke="#9aa5b4" stroke-width="1.5"><path d="M4 30 Q45 0 80 26"/><path d="M72 22 L80 26 L74 33"/></svg>
    <div class="step">
      <div class="ring"><svg width="44" height="44" viewBox="0 0 44 44" fill="#0455a3"><rect x="8" y="26" width="6" height="12"/><rect x="18" y="18" width="6" height="20"/><rect x="28" y="10" width="6" height="28"/></svg></div>
      See Results
    </div>
  </div>
  <a class="btn" href="#">Get Started</a>
</section>

<section class="improve center">
  <h2>We Help Improve Your<br><span class="accent">Credit Scores</span> By Removing:</h2>
  <div class="cards">
    <div class="card">
      <svg width="40" height="40" viewBox="0 0 40 40" fill="none" stroke="#0455a3" stroke-width="2.2"><rect x="5" y="8" width="30" height="26" rx="2"/><line x1="5" y1="16" x2="35" y2="16"/><line x1="12" y1="22" x2="28" y2="22"/><line x1="12" y1="28" x2="22" y2="28"/></svg>
      <h3>Collection Accounts</h3>
      <p>Lorem ipsum dolor sit amet, consectetuer adipiscing elit, sed diam nonummy nibh eluis.</p>
    </div>
    <div class="card active">
      <svg width="40" height="40" viewBox="0 0 40 40" fill="none" stroke="#ffffff" stroke-width="2.2"><path d="M6 26 L9 16 H31 L34 26 Z"/><rect x="5" y="26" width="30" height="6" rx="1"/><circle cx="12" cy="33" r="2"/><circle cx="28" cy="33" r="2"/></svg>
      <h3>Repossessions</h3>
      <p>Lorem ipsum dolor sit amet, consectetuer adipiscing elit, sed diam nonummy nibh eluis.</p>
    </div>
    <div class="card">
      <svg width="40" height="40" viewBox="0 0 40 40" fill="none" stroke="#0455a3" stroke-width="2.2"><circle cx="20" cy="24" r="11"/><path d="M15 10 L20 4 L25 10"/><line x1="20" y1="18" x2="20" y2="30"/><line x1="16" y1="24" x2="24" y2="24"/></svg>
      <h3>Charge offs</h3>
      <p>Lorem ipsum dolor sit amet, consectetuer adipiscing elit, sed diam nonummy nibh eluis.</p>
    </div>
    <div class="card">
      <svg width="40" height="40" viewBox="0 0 40 40" fill="none" stroke="#0455a3" stroke-width="2.2"><circle cx="15" cy="15" r="6"/><path d="M4 34 Q15 20 26 34"/><circle cx="30" cy="26" r="7"/><line x1="30" y1="22" x2="30" y2="27"/><line x1="30" y1="27" x2="33" y2="29"/></svg>
      <h3>Late payments</h3>
      <p>Lorem ipsum dolor sit amet, consectetuer adipiscing elit, sed diam nonummy nibh eluis.</p>
    </div>
    <div class="card">
      <svg width="40" height="40" viewBox="0 0 40 40" fill="none" stroke="#0455a3" stroke-width="2.2"><rect x="8" y="6" width="24" height="30" rx="2"/><rect x="14" y="3" width="12" height="6" rx="1"/><line x1="13" y1="18" x2="27" y2="18"/><line x1="13" y1="25" x2="27" y2="25"/></svg>
      <h3>Hard Inquiries</h3>
      <p>Lorem ipsum dolor sit amet, consectetuer adipiscing elit, sed diam nonummy nibh eluis.</p>
    </div>
    <div class="card">
      <svg width="40" height="40" viewBox="0 0 40 40" fill="none" stroke="#0455a3" stroke-width="2.2"><circle cx="20" cy="20" r="15"/><line x1="20" y1="12" x2="20" y2="28"/><line x1="12" y1="20" x2="28" y2="20"/></svg>
      <h3>And More +</h3>
      <p>Lorem ipsum dolor sit amet, consectetuer adipiscing elit, sed diam nonummy nibh eluis.</p>
    </div>
  </div>
  <a class="btn" href="#">Get Started</a>
</section>

<section class="guarantee" role="img" aria-label="Blue toned background of credit cards and a keyboard">
  <h2>We Have The Best 100%<br>Money Back Guarantee</h2>
  <p>We want it to catch the attention of the people as well as it be informative of the different types of derogatory items that can be listed on a report.</p>
  <a class="btn" href="#">Get Started</a>
</section>

<section class="pricing center">
  <div class="eyebrow">SAVE WITH OUR PRICING PACKAGES</div>
  <h2>Credit Repair <span class="accent">Made Affordable</span></h2>
  <div class="plans">
    <div class="plan">
      <svg width="60" height="60" viewBox="0 0 60 60" fill="none" stroke="#0455a3" stroke-width="2.4"><circle cx="30" cy="14" r="7"/><path d="M18 44 V32 Q30 20 42 32 V44"/><rect x="10" y="44" width="10" height="10"/><rect x="25" y="40" width="10" height="14"/><rect x="40" y="36" width="10" height="18"/></svg>
      <div class="price">$99<small>/m</small></div>
      <div class="sub">$99 Enrollment</div>
      <div class="term">Month-To-Month</div>
      <div class="includes">INCLUDES:</div>
      <ul class="features">
        <li>Unlimited Disputes</li><li>Unlimited Deletions</li><li>Flat Monthly Rate "No Contract"</li><li>24/7 Client Portal Access</li><li>Monthly Credit Analysis</li><li>Industry Leading Service</li>
      </ul>
      <a class="btn" href="#">Get Started</a>
    </div>
    <div class="plan">
      <svg width="60" height="60" viewBox="0 0 60 60" fill="none" stroke="#0455a3" stroke-width="2.4"><circle cx="20" cy="14" r="6"/><circle cx="40" cy="14" r="6"/><path d="M12 52 V28 Q20 20 28 28 V52"/><path d="M32 52 V28 Q40 20 48 28 V52"/></svg>
      <div class="price">$159<small>/m</small></div>
      <div class="sub">$129 Enrollment Each</div>
      <div class="term">Couple's Month-To-Month</div>
      <div class="includes">INCLUDES:</div>
      <ul class="features">
        <li>Unlimited Disputes</li><li>Unlimited Deletions</li><li>Flat Monthly Rate "No Contract"</li><li>24/7 Client Portal Access</li><li>Monthly Credit Analysis</li><li>Industry Leading Service</li>
      </ul>
      <a class="btn" href="#">Get Started</a>
    </div>
  </div>
</section>

<section class="faq center">
  <h2>Frequently <span class="accent">Asked Questions</span></h2>
  <div class="faq-list" style="text-align:left">
    <div class="faq-item">Lorem ipsum dolor sit amet, consectetuer?<span class="toggle"></span></div>
    <div class="faq-item open">
      <div class="q">Wisit esse molestie consequat?<span class="toggle"></span></div>
      <p>Lorem ipsum dolor sit amet, consectetuer adipiscing elit, sed diam nonummy nibh euismod tincidunt ut laoreet dolore magna aliquam erat volutpat. Ut wisi enim ad minim veniam.</p>
    </div>
    <div class="faq-item">Qui blandit praesent luptatum zzril?<span class="toggle"></span></div>
    <div class="faq-item">Delenit augue duis feugait nulla facilisi?<span class="toggle"></span></div>
    <div class="faq-item">Duis autem vel eum iriure dolor in hendrerit in vulputate?<span class="toggle"></span></div>
    <div class="faq-item">Illum dolore eu feugiat nulla facilisis?<span class="toggle"></span></div>
  </div>
</section>

<section class="inquiry center">
  <h2>Quick <span class="accent">Inquiry</span></h2>
  <div class="form" style="text-align:left">
    <div class="fields">
      <div class="field">Name*</div>
      <div class="field">Email*</div>
      <div class="field">Phone*</div>
    </div>
    <div class="field message">Message*</div>
  </div>
  <a class="btn" href="#">Submit Now</a>
</section>

<footer class="footer">
  <div class="mission">
    <h4>Our Mission</h4>
    <p>Lorem ipsum dolor sit amet, consectetuer adipiscing elit, sed diam nonummy nibh euismod tincidunt ut laoreet dolore magna aliquam erat volutpat. Ut wisi enim ad minim.</p>
  </div>
  <div>
    <h4>Quick Links</h4>
    <ul><li>Home</li><li>Pricing</li><li>Blog</li><li>About Us</li><li>Contact Us</li></ul>
  </div>
  <div class="contact">
    <h4>Contact Details</h4>
    <ul>
      <li><span class="ic"><svg width="10" height="12" viewBox="0 0 10 12" fill="#ffffff"><path d="M5 0 A4 4 0 0 1 9 4 C9 7 5 12 5 12 C5 12 1 7 1 4 A4 4 0 0 1 5 0Z"/></svg></span>Address Line Come Here 123<br>Address Line Come Here</li>
      <li><span class="ic"><svg width="10" height="10" viewBox="0 0 10 10" fill="#ffffff"><path d="M2 0 L4 2.5 L3 4 Q4.5 6 6 7 L7.5 6 L10 8 L8.5 10 Q3 9 0 1.5Z"/></svg></span>(555) 014-2290</li>
      <li><span class="ic"><svg width="12" height="9" viewBox="0 0 12 9" fill="none" stroke="#ffffff" stroke-width="1.2"><rect x="0.6" y="0.6" width="10.8" height="7.8"/><polyline points="0.6,0.6 6,5 11.4,0.6"/></svg></span>info@brevanta.example</li>
    </ul>
  </div>
  <div class="footer-brand">
    <div class="mark"></div>
    <div class="name">Brevanta Ledger</div>
    <div class="socials"><span></span><span></span><span></span></div>
  </div>
</footer>
<div class="copyright">Copyright 2020, Brevanta Ledger Partners. All Rights Reserved.</div>

</body>
</html>
```